CTWI application splash screen

We need a 1024x768 image for use as an application splash screen.
The image will be displayed full screen on an 10 inch industrial PC 1024x768 screen while our application is launching. The image should convey that the application is "Waiting for connection to Wi-Fi access point..." and include a graphic of the industrial PC connected to the access point via an Ethernet cable. A list of troubleshooting steps should be included at the bottom of the image. The troubleshooting steps should not be the main focus of the image and should be shown in a smaller font (but still readable at 1024x768 displayed on a 10 inch screen).
I will include a mock up of the general idea of what we are looking for as well as image files for the industrial PC, a screenshot of our application to show on the PC's screen and the AP.
For general look and feel and a sense of corporate branding please review our website https://corvanetillageworks.com/. The splash screen should reflect corporate branding.
Target Market(s)
Users of our application
Industry/Entity Type
Agriculture

```html
<!DOCTYPE html>
<html lang="en">
<head>
<meta charset="utf-8">
<title>CTWI – Waiting for Connection</title>
<link href="https://fonts.googleapis.com/css2?family=Arimo:wght@400;700&family=Roboto:wght@400;500;700&display=swap" rel="stylesheet">
<style>
  :root{
    --brand-green:#12b06a;
    --brand-green-dark:#0e9a5c;
    --ink:#262626;
    --ink-soft:#3a3a3a;
    --dot-idle:#d4d4d4;
    --rule:#3b3b3b;
    --paper:#ffffff;
    --device-dark:#232425;
    --device-screen:#e9efe9;
    --ap-body:#f1f2f3;
  }
  html,body{margin:0;padding:0;overflow:hidden;background:var(--paper);}
  .splash{
    position:relative;width:1200px;height:900px;overflow:hidden;
    background:var(--paper);color:var(--ink);
    font-family:"Arimo",Arial,sans-serif;
  }
  .abs{position:absolute;}

  .brand-name{
    left:33px;top:26px;width:111px;height:115px;
    display:flex;align-items:center;justify-content:center;
    font-family:"Arimo",Arial,sans-serif;font-weight:700;font-size:34px;
    color:var(--brand-green);letter-spacing:1px;
  }

  .wifi-icon{left:555px;top:26px;width:94px;height:70px;}

  .headline-top,.headline-main,.headline-sub{
    left:0;width:1200px;text-align:center;margin:0;
  }
  .headline-top{top:139px;font-size:33px;letter-spacing:0.52em;font-weight:400;color:var(--ink);padding-left:0.5em;box-sizing:border-box;}
  .headline-main{top:182px;font-size:76px;font-weight:400;letter-spacing:0.07em;color:var(--brand-green);line-height:1;-webkit-text-stroke:1.4px var(--brand-green);}
  .headline-sub{top:267px;font-size:33px;letter-spacing:0.2em;color:var(--ink);padding-left:0.2em;box-sizing:border-box;}

  .progress{left:525px;top:352px;display:flex;gap:17px;}
  .progress span{width:18px;height:18px;border-radius:50%;background:var(--dot-idle);}
  .progress span.is-active{background:var(--brand-green);}

  .device-computer{
    left:72px;top:358px;width:269px;height:214px;border-radius:14px;
    background:linear-gradient(160deg,#3a3b3c,var(--device-dark));
  }
  .device-computer .screen-area{
    position:absolute;left:25px;top:20px;width:219px;height:162px;border-radius:2px;
    background:linear-gradient(180deg,var(--device-screen),#cfe7d6);
  }
  .device-ap{
    left:992px;top:215px;width:56px;height:365px;border-radius:10px;
    background:linear-gradient(90deg,#e4e6e8,var(--ap-body) 45%,#dcdfe1);
  }
  .ap-rings{left:873px;top:267px;width:284px;height:284px;}

  .link-line{left:436px;top:465px;width:440px;height:24px;}
  .port-badge{width:68px;height:68px;}
  .port-left{left:360px;top:445px;}
  .port-right{left:884px;top:440px;}

  .cable-label{
    left:547px;top:422px;width:189px;height:30px;background:var(--brand-green);
    color:#fff;font-weight:700;font-size:19px;letter-spacing:0.05em;
    display:flex;align-items:center;justify-content:center;
  }
  .cable-label::after{
    content:"";position:absolute;left:83px;top:30px;
    border-left:10px solid transparent;border-right:10px solid transparent;
    border-top:11px solid var(--brand-green);
  }

  .caption{font-weight:700;font-size:17.5px;letter-spacing:0.06em;color:var(--ink-soft);margin:0;}
  .caption-computer{left:86px;top:600px;}
  .caption-ap{left:935px;top:606px;}
  .caption-model{left:962px;top:626px;font-size:12px;color:var(--ink);letter-spacing:0.02em;}

  .divider{left:51px;top:647px;width:1074px;height:1.5px;background:var(--rule);}

  .tools-icon{left:55px;top:702px;width:72px;height:72px;}
  .trouble-title{
    left:139px;top:720px;margin:0;font-family:"Roboto",Arial,sans-serif;font-weight:700;
    font-size:20.5px;line-height:24px;letter-spacing:0.05em;color:var(--ink-soft);
  }
  .trouble-rule{left:320px;top:680px;width:1px;height:141px;background:var(--rule);}

  .steps{left:336px;top:682px;margin:0;padding:0;list-style:none;font-size:14.6px;color:var(--ink);}
  .steps li{position:relative;padding-left:22px;height:24.5px;line-height:20px;}
  .steps li::before{content:"";position:absolute;left:0;top:6px;width:7px;height:7px;border-radius:50%;background:var(--ink);}
  .steps .sub{list-style:none;margin:0;padding:0 0 0 14px;}
  .steps .sub li::before{width:5px;height:5px;top:8px;}

  .tagline{
    left:0;width:1200px;top:864px;margin:0;text-align:center;font-weight:700;font-size:19px;
    letter-spacing:0.55em;color:#111;padding-left:0.55em;box-sizing:border-box;
  }
</style>
</head>
<body>
<main class="splash">

  <div class="abs brand-name">CTWI</div>

  <svg class="abs wifi-icon" viewBox="0 0 94 70" aria-hidden="true">
    <g fill="none" stroke="var(--brand-green)" stroke-width="8" stroke-linecap="round">
      <path d="M5 22 Q47 -10 89 22"/>
      <path d="M17 36 Q47 13 77 36"/>
      <path d="M30 50 Q47 37 64 50"/>
    </g>
    <circle cx="47" cy="60" r="6" fill="var(--brand-green)"/>
  </svg>

  <p class="abs headline-top">WAITING FOR</p>
  <h1 class="abs headline-main">CONNECTION</h1>
  <p class="abs headline-sub">TO WI-FI ACCESS POINT...</p>

  <div class="abs progress" aria-label="Loading progress">
    <span class="is-active"></span><span></span><span></span><span></span><span></span>
  </div>

  <div class="abs device-computer" role="img" aria-label="Photo of the rugged tractor cab computer showing the seed sensing application">
    <div class="screen-area"></div>
  </div>

  <svg class="abs ap-rings" viewBox="0 0 284 284" aria-hidden="true">
    <g fill="none" stroke="#eef0ef" stroke-width="1.5">
      <circle cx="142" cy="142" r="72"/>
      <circle cx="142" cy="142" r="106"/>
      <circle cx="142" cy="142" r="140"/>
    </g>
  </svg>
  <div class="abs device-ap" role="img" aria-label="Photo of the white outdoor Wi-Fi access point with two antennas"></div>

  <svg class="abs link-line" viewBox="0 0 440 24" aria-hidden="true">
    <line x1="7" y1="12" x2="433" y2="12" stroke="var(--brand-green)" stroke-width="3"/>
    <circle cx="7" cy="12" r="5" fill="var(--brand-green)"/>
    <circle cx="433" cy="12" r="5" fill="var(--brand-green)"/>
  </svg>

  <svg class="abs port-badge port-left" viewBox="0 0 68 68" aria-hidden="true">
    <circle cx="34" cy="34" r="32" fill="none" stroke="var(--brand-green)" stroke-width="2"/>
    <circle cx="34" cy="34" r="27" fill="none" stroke="var(--brand-green)" stroke-width="4"/>
    <rect x="20" y="21" width="28" height="22" rx="3" fill="var(--brand-green)"/>
    <rect x="24" y="26" width="20" height="6" fill="#fff"/>
    <g stroke="var(--brand-green)" stroke-width="2"><path d="M28 26v6M32 26v6M36 26v6M40 26v6"/></g>
    <g stroke="var(--brand-green)" stroke-width="3" stroke-linecap="round"><path d="M26 43v6M31 43v7M37 43v7M42 43v6"/></g>
  </svg>
  <svg class="abs port-badge port-right" viewBox="0 0 68 68" aria-hidden="true">
    <circle cx="34" cy="34" r="32" fill="none" stroke="var(--brand-green)" stroke-width="2"/>
    <circle cx="34" cy="34" r="27" fill="none" stroke="var(--brand-green)" stroke-width="4"/>
    <rect x="20" y="21" width="28" height="22" rx="3" fill="var(--brand-green)"/>
    <rect x="24" y="26" width="20" height="6" fill="#fff"/>
    <g stroke="var(--brand-green)" stroke-width="2"><path d="M28 26v6M32 26v6M36 26v6M40 26v6"/></g>
    <g stroke="var(--brand-green)" stroke-width="3" stroke-linecap="round"><path d="M26 43v6M31 43v7M37 43v7M42 43v6"/></g>
  </svg>

  <div class="abs cable-label">ETHERNET CABLE</div>

  <p class="abs caption caption-computer">TRACTOR CAB COMPUTER</p>
  <p class="abs caption caption-ap">WI-FI ACCESS POINT</p>
  <p class="abs caption caption-model">Norvik AX-220 Outdoor</p>

  <div class="abs divider"></div>

  <svg class="abs tools-icon" viewBox="0 0 72 72" aria-hidden="true">
    <circle cx="36" cy="36" r="34" fill="none" stroke="var(--ink-soft)" stroke-width="3"/>
    <g fill="none" stroke="var(--ink-soft)" stroke-width="3" stroke-linecap="round" stroke-linejoin="round">
      <path d="M18 18l4-3 6 6-3 4z"/>
      <path d="M26 24l24 24"/>
      <rect x="45" y="44" width="9" height="14" rx="2" transform="rotate(-45 49.5 51)"/>
      <path d="M52 16a8 8 0 0 0-9 11L18 52a3 3 0 0 0 4 4l25-25a8 8 0 0 0 11-9l-5 5-5-1-1-5z"/>
    </g>
  </svg>
  <h2 class="abs trouble-title">Troubleshooting<br>steps:</h2>
  <div class="abs trouble-rule"></div>

  <ul class="abs steps">
    <li>This screen should only be visible for a short time on boot.</li>
    <li>If this screen stays visible for more than a minute:</li>
    <li style="padding:0;height:auto;">
      <ul class="sub">
        <li>Verify that the Wi-Fi Access Point (AP) powers up when this system does (indicated by a green light on the side of the AP).</li>
        <li>Check the Ethernet cable between this system and the AP for damage, and replace it if necessary.</li>
        <li>Power-cycle this system and wait for it to reboot fully.</li>
        <li>If the issue persists, contact CTWI support for further assistance.</li>
      </ul>
    </li>
  </ul>

  <p class="abs tagline">SEED SENSING SYSTEM</p>
</main>
</body>
</html>
```